The Timber Loft

We need a business card design for our wardrobe company.
Please visit our website www.zorvelcabinets.com to get an idea of who we are.

```html
<!DOCTYPE html>
<html lang="en">
<head>
<meta charset="utf-8">
<title>The Timber Loft – Business Card</title>
<link href="https://fonts.googleapis.com/css2?family=Montserrat:wght@400&family=Carlito:wght@400&display=swap" rel="stylesheet">
<style>
  :root {
    --stage: #8cc9bc;
    --card: #151515;
    --card-deep: #0b0b0b;
    --card-warm: #242120;
    --frame: rgba(200, 200, 200, 0.55);
    --ink: #ffffff;
    --ink-soft: #f2f2f2;
  }
  * { margin: 0; padding: 0; box-sizing: border-box; }
  html, body {
    width: 1200px;
    height: 800px;
    overflow: hidden;
  }
  body {
    background: var(--stage);
    position: relative;
  }
  .business-card {
    position: absolute;
    left: 255px;
    top: 200px;
    width: 690px;
    height: 400px;
    border-radius: 18px;
    background: var(--card);
    overflow: hidden;
    box-shadow: 0 14px 30px rgba(0, 0, 0, 0.25);
  }
  .wardrobe-backdrop {
    position: absolute;
    inset: 0;
    background:
      linear-gradient(90deg, rgba(255,255,255,0.02) 0%, rgba(255,255,255,0.05) 45%, rgba(255,255,255,0.02) 100%),
      linear-gradient(180deg, var(--card-warm) 0%, var(--card) 45%, var(--card-deep) 100%);
  }
  .inner-frame {
    position: absolute;
    inset: 14px;
    border: 2px solid var(--frame);
    border-radius: 12px;
  }
  .brand-mark {
    position: absolute;
    left: 172px;
    top: 82px;
    width: 84px;
    height: 84px;
    border: 3px solid var(--ink);
  }
  .brand-name {
    position: absolute;
    left: 285px;
    top: 86px;
    font-family: "Montserrat", sans-serif;
    font-weight: 400;
    font-size: 24px;
    letter-spacing: 0.5px;
    color: var(--ink);
    text-transform: uppercase;
    white-space: nowrap;
  }
  .tagline {
    position: absolute;
    left: 288px;
    top: 126px;
    font-family: "Montserrat", sans-serif;
    font-weight: 400;
    font-size: 22px;
    color: var(--ink);
    white-space: nowrap;
  }
  .contact-list {
    position: absolute;
    left: 0;
    right: 0;
    top: 252px;
    list-style: none;
    font-family: "Carlito", sans-serif;
    font-size: 17px;
    color: var(--ink-soft);
    text-align: center;
  }
  .contact-list li {
    height: 24px;
    display: flex;
    align-items: center;
    justify-content: center;
    gap: 8px;
    white-space: nowrap;
  }
  .contact-icon {
    width: 12px;
    height: 12px;
    fill: var(--ink-soft);
  }
</style>
</head>
<body>
  <div class="business-card">
    <div class="wardrobe-backdrop" role="img" aria-label="Dark photograph of a wardrobe interior with hanging clothes"></div>
    <div class="inner-frame"></div>

    <div class="brand-mark"></div>
    <div class="brand-name">The Timber Loft</div>
    <div class="tagline">Built True, Made to Measure</div>

    <ul class="contact-list">
      <li>
        <svg class="contact-icon" viewBox="0 0 12 12" aria-hidden="true"><path d="M6 0.5a3.8 3.8 0 0 0-3.8 3.8C2.2 7.2 6 11.5 6 11.5s3.8-4.3 3.8-7.2A3.8 3.8 0 0 0 6 0.5zm0 5.3a1.5 1.5 0 1 1 0-3 1.5 1.5 0 0 1 0 3z"/></svg>
        Alder Court, 42 Marlow Lane, Brentham BR4 7QT
      </li>
      <li>
        <svg class="contact-icon" viewBox="0 0 12 12" aria-hidden="true"><path d="M1 4c0-1.6 2.2-2.6 5-2.6S11 2.4 11 4v1H8.5V3.8H3.5V5H1zM2.5 6h7l1 4.5h-9z"/></svg>
        0161 555 0428
      </li>
      <li>
        <svg class="contact-icon" viewBox="0 0 12 12" aria-hidden="true"><path d="M0.5 2.5h11v7h-11zM1.5 3.3 6 6.6l4.5-3.3z" fill-rule="evenodd"/></svg>
        info@zorvelcabinets.com
      </li>
      <li>
        <svg class="contact-icon" viewBox="0 0 12 12" aria-hidden="true"><path d="M6 0.5a5.5 5.5 0 1 0 0 11 5.5 5.5 0 0 0 0-11zm0 1.3c1 0 1.9 1.6 2 3.6H4c.1-2 1-3.6 2-3.6zM4 6.6h4c-.1 2-1 3.6-2 3.6s-1.9-1.6-2-3.6z"/></svg>
        www.zorvelcabinets.com
      </li>
    </ul>
  </div>
</body>
</html>
```